Business Card/Stationary
General Contractor
Thank You for all of the submissions so far.
I have eliminated those that had too many curved lines. I like any lines to be more perpendicular/parallel. However, I have left a few with curved lines that I like.
I do like the solid colors on the front and or back.
I have not seen any stationary submissions. I need some of those as well, although not as critical as a business card.
Thank You for your submissions. I will comment again in a couple of days.

```html
<!DOCTYPE html>
<html lang="en">
<head>
<meta charset="utf-8">
<title>Tarnley Builders — Business Card Presentation</title>
<link href="https://fonts.googleapis.com/css2?family=Arimo:wght@400;700&family=Cinzel:wght@400&display=swap" rel="stylesheet">
<style>
  :root {
    --page: #ffffff;
    --label: #6f6f6f;
    --ink: #3a3a3a;
    --ink-soft: #777777;
    --accent-blue: #1f5fb0;
    --accent-orange: #f07a1a;
    --white: #ffffff;
    --blue-light: #3f87d6;
    --blue-dark: #0b3f8c;
    --orange-light: #ffb238;
    --orange-dark: #ea6a12;
    --gray-light: #9a9a9a;
    --gray-dark: #5c5c5c;
    --front-light: #ffffff;
    --front-dark: #e9e9e9;
  }
  * { margin: 0; padding: 0; box-sizing: border-box; }
  html, body { width: 1200px; height: 874px; overflow: hidden; background: var(--page); }
  .board { position: relative; width: 1200px; height: 874px; font-family: "Arimo", Arial, sans-serif; }

  .side-label {
    position: absolute; width: 470px; text-align: center;
    font-family: "Cinzel", "Times New Roman", serif; font-size: 34px;
    color: var(--label); letter-spacing: 1px;
  }

  .card {
    position: absolute; width: 470px; height: 300px; overflow: hidden;
    box-shadow: 0 14px 18px -10px rgba(0,0,0,0.35);
  }
  .card--front { background: radial-gradient(ellipse at 40% 40%, var(--front-light) 30%, var(--front-dark) 100%); }
  .card--blue { background: radial-gradient(ellipse at 35% 45%, var(--blue-light) 0%, var(--blue-dark) 85%); }
  .card--orange { background: radial-gradient(ellipse at 30% 45%, var(--orange-light) 0%, var(--orange-dark) 75%); }
  .card--gray { background: radial-gradient(ellipse at 35% 45%, var(--gray-light) 0%, var(--gray-dark) 85%); }

  /* Front */
  .brand { position: absolute; left: 52px; top: 108px; display: flex; align-items: center; gap: 8px; }
  .brand-square { width: 34px; height: 34px; background: var(--accent-orange); }
  .brand-name { font-size: 26px; font-weight: 700; color: var(--ink); line-height: 1; }
  .brand-sub { position: absolute; left: 94px; top: 146px; font-size: 10px; color: var(--ink-soft); letter-spacing: 1px; }

  .divider { position: absolute; left: 238px; top: 60px; width: 2px; height: 170px; background: var(--accent-blue); }

  .contact { position: absolute; left: 252px; top: 72px; color: var(--ink); }
  .contact-name { font-size: 15px; color: var(--accent-blue); }
  .contact-title { font-size: 10px; color: var(--ink-soft); margin-top: 3px; }
  .contact-lines { margin-top: 28px; font-size: 9px; line-height: 12.5px; color: var(--ink-soft); list-style: none; }

  /* Back */
  .back-mark { position: absolute; left: 48px; top: 82px; display: flex; flex-direction: column; align-items: flex-start; gap: 6px; }
  .back-mark-square { width: 44px; height: 44px; background: var(--white); }
  .back-mark-name { font-size: 13px; color: var(--white); }

  .services { position: absolute; left: 138px; top: 84px; color: var(--white); list-style: none; }
  .services-heading { font-size: 15px; margin-bottom: 3px; }
  .services li { font-size: 11px; line-height: 13px; }
</style>
</head>
<body>
<main class="board">

  <div class="side-label" style="left:120px; top:92px;">FRONT</div>
  <div class="side-label" style="left:640px; top:92px;">BACK</div>
  <div class="side-label" style="left:120px; top:498px;">BACK</div>
  <div class="side-label" style="left:640px; top:498px;">BACK</div>

  <section class="card card--front" style="left:120px; top:156px;">
    <div class="brand">
      <span class="brand-square"></span>
      <span class="brand-name">tarnley</span>
    </div>
    <div class="brand-sub">BUILDERS, LLC</div>
    <div class="divider"></div>
    <div class="contact">
      <div class="contact-name">ElBayu KorvMint</div>
      <div class="contact-title">President</div>
      <ul class="contact-lines">
        <li>4170 Harbor Crest Avenue</li>
        <li>Suite 210 Lakewood, FL 33019</li>
        <li>P: 555.214.0380</li>
        <li>C: 555.637.1942</li>
        <li>F: 555.880.2096</li>
        <li>E: elbayu@tarnleybuilders.com</li>
        <li>tarnleybuilders.com</li>
        <li>License No. CGC 1048263</li>
      </ul>
    </div>
  </section>

  <section class="card card--blue" style="left:640px; top:156px;">
    <div class="back-mark"><span class="back-mark-square"></span><span class="back-mark-name">Tarnley</span></div>
    <ul class="services">
      <li class="services-heading">General Contractor</li>
      <li>Construction Management</li>
      <li>Disaster Response</li>
      <li>Fire/Water/Smoke Damage Restoration</li>
      <li>Mold Assessment/Remediation/Prevention</li>
    </ul>
  </section>

  <section class="card card--orange" style="left:120px; top:557px;">
    <div class="back-mark"><span class="back-mark-square"></span><span class="back-mark-name">Tarnley</span></div>
    <ul class="services">
      <li class="services-heading">General Contractor</li>
      <li>Construction Management</li>
      <li>Disaster Response</li>
      <li>Fire/Water/Smoke Damage Restoration</li>
      <li>Mold Assessment/Remediation/Prevention</li>
    </ul>
  </section>

  <section class="card card--gray" style="left:640px; top:557px;">
    <div class="back-mark"><span class="back-mark-square"></span><span class="back-mark-name">Tarnley</span></div>
    <ul class="services">
      <li class="services-heading">General Contractor</li>
      <li>Construction Management</li>
      <li>Disaster Response</li>
      <li>Fire/Water/Smoke Damage Restoration</li>
      <li>Mold Assessment/Remediation/Prevention</li>
    </ul>
  </section>

</main>
</body>
</html>
```